Hot Offer banner for product listing page

Hi, we need a banner in the dimensions 210x390px which will be shown in the product listing on our online shop. There are 18 products and in between randomly there should be 3 banners with three different information.
first banner: fast delivery
The idea is to show a stove which is very "fast". Maybe you can make an effect like in Voidcruiser Halcyon when they activate the warp drive or something similar. Anyway, the banner should indicate that the delivery is very fast for this product.

second banner: Advantage banner
We would like to have a banner which names all our advantages in our online shop. this is the list of advantages:
- over 200,000 satisfied customers
- Best price guarantee
- thousands of devices in stock
- Top ratings

I attached you some examples, just to give you an idea.

```html
<!DOCTYPE html>
<html lang="de">
<head>
<meta charset="utf-8">
<title>Kaminofen Banner</title>
<link rel="stylesheet" href="https://fonts.googleapis.com/css2?family=Russo+One&display=swap">
<style>
  :root {
    --stage: #4d4d4d;
    --paper: #f7f7f7;
    --blue: #0a8bcb;
    --yellow: #ffcc00;
    --orange: #ff7d0e;
    --white: #ffffff;
    --stove: #3a3b3d;
    --stove-side: #a9aaab;
  }
  html, body {
    margin: 0;
    width: 1200px;
    height: 1200px;
    overflow: hidden;
    background: var(--stage);
  }
  .banner {
    position: absolute;
    top: 218px;
    width: 410px;
    height: 763px;
    display: block;
  }
  .banner--delivery { left: 142px; }
  .banner--advantages { left: 648px; }
  .headline {
    font-family: "Russo One", "Arial Black", sans-serif;
    fill: var(--white);
  }
  .headline--blue { fill: url(#stripe-blue); }
  .fill-paper { fill: var(--paper); }
  .fill-blue { fill: var(--blue); }
  .fill-yellow { fill: var(--yellow); }
  .fill-orange { fill: var(--orange); }
  .speed-lines line { stroke-width: 3; stroke-linecap: round; }
  .speed-lines--white line { stroke: var(--white); }
  .speed-lines--blue line { stroke: var(--blue); }
</style>
</head>
<body>

<!-- Banner 1: fast delivery -->
<svg class="banner banner--delivery" viewBox="0 0 513 954" xmlns="http://www.w3.org/2000/svg">
  <defs>
    <pattern id="stripe-blue" width="6" height="6" patternUnits="userSpaceOnUse">
      <rect width="6" height="6" fill="#0a8bcb"/>
      <rect y="4" width="6" height="1.2" fill="#ffcc00"/>
    </pattern>
  </defs>
  <rect class="fill-paper" width="513" height="954"/>
  <polygon class="fill-blue" points="0,450 513,665 513,954 0,954"/>
  <polygon class="fill-yellow" points="513,420 513,665 340,592"/>

  <g class="product-photo" role="img" aria-label="Photo of a round black wood-burning stove with grey stone side panels, a flue pipe on top, a glass fire door and stacked firewood in the base">
    <rect x="228" y="0" width="78" height="230" fill="#333436"/>
    <rect x="106" y="218" width="312" height="705" rx="18" fill="var(--stove-side)"/>
    <rect x="122" y="240" width="260" height="680" rx="14" fill="var(--stove)"/>
  </g>

  <polygon class="fill-orange" points="60,488 513,423 485,505 33,568"/>
  <polygon class="fill-orange" points="28,628 463,566 438,643 1,708"/>

  <g class="speed-lines speed-lines--white">
    <line x1="75" y1="565" x2="150" y2="555"/>
    <line x1="68" y1="578" x2="150" y2="567"/>
    <line x1="62" y1="591" x2="150" y2="579"/>
    <line x1="56" y1="604" x2="150" y2="591"/>
  </g>

  <text class="headline" font-size="60" textLength="440" lengthAdjust="spacingAndGlyphs"
        transform="translate(63 550) rotate(-8) skewX(-12)">KAMINOFEN</text>
  <text class="headline headline--blue" font-size="54" textLength="280" lengthAdjust="spacingAndGlyphs"
        transform="translate(156 597) rotate(-8) skewX(-12)">SOFORT</text>
  <text class="headline" font-size="60" textLength="395" lengthAdjust="spacingAndGlyphs"
        transform="translate(36 683) rotate(-8) skewX(-12)">LIEFERBAR</text>
</svg>

<!-- Banner 2: shop advantages -->
<svg class="banner banner--advantages" viewBox="0 0 513 954" xmlns="http://www.w3.org/2000/svg">
  <rect class="fill-yellow" width="513" height="954"/>
  <polygon class="fill-orange" points="0,593 513,453 513,954 0,954"/>

  <polygon class="fill-orange" points="45,353 488,231 465,313 23,448"/>
  <polygon class="fill-blue" points="155,418 470,340 452,418 135,508"/>
  <polygon class="fill-orange" points="70,575 472,433 462,475 60,612"/>
  <polygon class="fill-blue" points="120,633 480,536 460,608 100,698"/>

  <g class="speed-lines speed-lines--blue">
    <line x1="70" y1="455" x2="148" y2="435"/>
    <line x1="62" y1="470" x2="145" y2="449"/>
    <line x1="55" y1="485" x2="142" y2="463"/>
    <line x1="48" y1="500" x2="138" y2="477"/>
    <line x1="40" y1="515" x2="135" y2="491"/>
    <line x1="30" y1="665" x2="115" y2="643"/>
    <line x1="25" y1="680" x2="112" y2="657"/>
    <line x1="20" y1="695" x2="108" y2="671"/>
    <line x1="15" y1="710" x2="105" y2="685"/>
  </g>

  <text class="headline" font-size="26" textLength="82" lengthAdjust="spacingAndGlyphs"
        transform="translate(68 395) rotate(-15) skewX(-12)">Over</text>
  <text class="headline" font-size="62" textLength="305" lengthAdjust="spacingAndGlyphs"
        transform="translate(158 370) rotate(-15) skewX(-12)">200,000</text>
  <text class="headline" font-size="30" textLength="395" lengthAdjust="spacingAndGlyphs"
        transform="translate(58 425) rotate(-15) skewX(-12)">Satisfied Customers</text>

  <text class="headline" font-size="44" textLength="290" lengthAdjust="spacingAndGlyphs"
        transform="translate(162 460) rotate(-15) skewX(-12)">Best Price</text>
  <text class="headline" font-size="44" textLength="290" lengthAdjust="spacingAndGlyphs"
        transform="translate(152 500) rotate(-15) skewX(-12)">Guarantee</text>

  <text class="headline" font-size="52" textLength="345" lengthAdjust="spacingAndGlyphs"
        transform="translate(95 580) rotate(-15) skewX(-12)">Thousands</text>
  <text class="headline" font-size="28" textLength="345" lengthAdjust="spacingAndGlyphs"
        transform="translate(75 620) rotate(-15) skewX(-12)">of devices in stock</text>

  <text class="headline" font-size="50" textLength="335" lengthAdjust="spacingAndGlyphs"
        transform="translate(135 680) rotate(-15) skewX(-12)">Top Ratings</text>
</svg>

</body>
</html>
```